Classy, Elegant, Simple Business Card Design

Looking to have a classy, simple, and elegant design. Want a top notch designed business card. I really like the look of the new brivo credit card. I also like the design I attached. I am trying to reach 21-29 year old females for booking us for there wedding or event. We offer Disc Jockey Service, Photo Booth Rentals, and Uplighting .

Target Market(s)

21-28 year old females

Contact Information for Business Card

Has to have logo, website, email, and phone number

Font styles to use
Other font styles liked:
• open to font choice, modern, clean
Designer to choose
33a6d7
0791cd
0555a3
ffffff

Requirements
Must have
• Has to have logo, website, email, and phone number
Nice to have
• I really like the design of the new brivo credit card. I also included my logo and some designs I like
Should not have
• clutter or too much info

```html
<!DOCTYPE html>
<html lang="en">
<head>
<meta charset="utf-8">
<title>Tidewell Event Group – Business Card</title>
<link href="https://fonts.googleapis.com/css2?family=Montserrat:wght@400;500;600;700&display=swap" rel="stylesheet">
<style>
  :root {
    --page-bg: #f3f4f5;
    --card-bg: #ffffff;
    --card-edge: #e3e5e7;
    --ink-dark: #3a3c3f;
    --ink-mid: #55585c;
    --ink-soft: #8a8d91;
    --brand-sky: #33a6d7;
    --brand-blue: #0791cd;
    --brand-navy: #0555a3;
  }
  * { box-sizing: border-box; margin: 0; padding: 0; }
  html, body {
    width: 1102px;
    height: 1200px;
    overflow: hidden;
    background: var(--page-bg);
    font-family: "Montserrat", Arial, sans-serif;
  }
  .canvas {
    position: relative;
    width: 1102px;
    height: 1200px;
  }
  .card {
    position: absolute;
    left: 171px;
    width: 760px;
    height: 480px;
    background: var(--card-bg);
    border: 1px solid var(--card-edge);
    border-radius: 26px;
    box-shadow: 0 18px 40px rgba(0, 0, 0, 0.10), 0 3px 8px rgba(0, 0, 0, 0.06);
  }
  .card--back { top: 80px; }
  .card--front { top: 640px; }

  /* Back side */
  .back__mark {
    position: absolute;
    top: 52px;
    right: 60px;
    font-size: 22px;
    font-weight: 600;
    letter-spacing: 3px;
    color: var(--ink-mid);
  }
  .back__person {
    position: absolute;
    left: 60px;
    top: 210px;
  }
  .back__name {
    font-size: 30px;
    font-weight: 700;
    color: var(--ink-dark);
  }
  .back__title {
    margin-top: 6px;
    font-size: 15px;
    font-weight: 600;
    letter-spacing: 1px;
    color: var(--ink-mid);
  }
  .back__contact {
    position: absolute;
    left: 60px;
    bottom: 52px;
    list-style: none;
    font-size: 17px;
    font-weight: 500;
    color: var(--ink-mid);
  }
  .back__contact li {
    display: flex;
    gap: 18px;
    line-height: 32px;
  }
  .back__contact .label { width: 22px; }

  /* Front side */
  .front__brand {
    position: absolute;
    inset: 0;
    display: flex;
    align-items: center;
    justify-content: center;
    gap: 18px;
  }
  .front__dot {
    width: 26px;
    height: 26px;
    border-radius: 50%;
    background: var(--brand-blue);
  }
  .front__name {
    font-size: 38px;
    font-weight: 600;
    letter-spacing: 3px;
    color: var(--brand-blue);
  }
</style>
</head>
<body>
  <main class="canvas">
    <section class="card card--back" aria-label="Business card back">
      <div class="back__mark">TIDEWELL</div>
      <div class="back__person">
        <p class="back__name">Your Name</p>
        <p class="back__title">JOB TITLE</p>
      </div>
      <ul class="back__contact">
        <li><span class="label">P:</span><span>000 000 0000</span></li>
        <li><span class="label">E:</span><span>youremail@xyz.com</span></li>
        <li><span class="label">W:</span><span>www.yourwebsite.com</span></li>
      </ul>
    </section>

    <section class="card card--front" aria-label="Business card front">
      <div class="front__brand">
        <span class="front__dot"></span>
        <span class="front__name">Tidewell Event Group</span>
      </div>
    </section>
  </main>
</body>
</html>
```